Flyer-Design für psychologische Beratung und Therapie
Zielgruppe
In meiner Praxis für psychologische Beratung und Therapie unterstütze ich Menschen dabei, ihre Probleme zu lösen. Schwerpunkte sind die Stärkung des Selbstwertgefühls, Überwindung von Ängsten und Krisen.
Aufgabenstellung
Din lang 4-Seitig
(Zitat)
'Bei aller Ernsthaftigkeit und Empathie dürfen Leichtigkeit,
Zuversicht und Humor in der Therapie nicht zu kurz kommen.“
(Text)
Mein Name ist Klaus Dieter Wabe, ich bin Transaktionsanalytiker, psychotherapeutischer Heilpraktiker und begeisterter LUM® Therapeut. Wenn Sie zufriedener leben wollen, neue Wege einschlagen oder sich beruflich oder persönlich weiterentwickeln wollen, begleite ich Sie gern dabei!
Möchten Sie ein stärkeres Selbstwertgefühl entwickeln, Ängste reduzieren oder eine akute Krise überwinden? Oder geeignete Strategien entwickeln, damit Sie Ihren Beruf zufriedener und erfolgreicher ausüben können? Auf dem Weg zu Ihrem Ziel biete ich Ihnen Unterstützung, vereinbaren Sie gerne einen ersten Termin!

```html
<!DOCTYPE html>
<html lang="de">
<head>
<meta charset="utf-8">
<title>Psychologische Beratung und Therapie – Flyer</title>
<link href="https://fonts.googleapis.com/css2?family=Open+Sans:ital,wght@0,400;0,600;0,700;1,400;1,600&display=swap" rel="stylesheet">
<style>
  :root {
    --accent: #f0a80c;
    --panel: #edb110;
    --ink: #5a5a5a;
    --rule: #cfcfcf;
    --paper: #ffffff;
    --white: #ffffff;
  }
  * { margin: 0; padding: 0; box-sizing: border-box; }
  html, body { width: 1200px; height: 1200px; overflow: hidden; background: var(--paper); }
  body { font-family: "Open Sans", Arial, sans-serif; color: var(--ink); }
  .flyer { position: relative; width: 1200px; height: 1200px; }
  .abs { position: absolute; }
  .hl { color: var(--accent); }

  .title { left: 52px; top: 44px; font-size: 41px; line-height: 49px; font-weight: 600; color: var(--accent); }
  .intro { left: 52px; top: 175px; font-size: 19px; line-height: 24.4px; }

  .rule { height: 1px; background: var(--rule); }

  .section-icon { width: 44px; height: 44px; }
  .section-head { font-size: 24px; line-height: 29px; font-weight: 700; color: var(--ink); }

  .person { left: 52px; top: 463px; font-size: 20px; line-height: 24.4px; font-weight: 600; color: var(--accent); }
  .person strong { font-weight: 700; }

  .photo { left: 52px; top: 659px; width: 500px; height: 331px;
    background: linear-gradient(180deg, #cbb99a 0%, #e6d3ae 35%, #d8b47a 62%, #6f6b43 82%, #4d4a30 100%); }
  .promise { left: 46px; top: 944px; width: 512px; height: 191px; background: var(--panel);
    color: var(--white); font-size: 19px; line-height: 24.4px; padding: 21px 0 0 23px; }
  .promise strong { font-weight: 700; }

  .quote-mark { left: 654px; top: 56px; }
  .quote { left: 716px; top: 56px; font-size: 19px; line-height: 24.4px; font-style: italic; color: var(--accent); }

  .offer { left: 650px; top: 322px; width: 513px; height: 203px; background: var(--panel); padding-top: 33px; }
  .offer li { list-style: none; position: relative; padding-left: 54px; font-size: 24px; line-height: 40.7px;
    font-style: italic; font-weight: 600; color: var(--white); }
  .offer li::before { content: ""; position: absolute; left: 22px; top: 18px; width: 6px; height: 6px;
    border-radius: 50%; background: var(--white); }

  .method-title { font-size: 17.5px; line-height: 22px; font-weight: 700; color: var(--accent); }
  .method-text { font-size: 17px; line-height: 22px; }
</style>
</head>
<body>
<main class="flyer">

  <h1 class="abs title">Psychologische<br>Beratung und Therapie</h1>

  <p class="abs intro">Brauchen Sie <span class="hl">Unterstützung</span> bei der Bewältigung<br>
  einer Krise oder möchten Sie sich von Ängsten, Lam-<br>
  penfieber oder Prüfungsangst <span class="hl">befreien</span>?<br>
  Vielleicht möchten Sie etwas <span class="hl">Neues</span> entwickeln: ein<br>
  <span class="hl">stärkeres Selbstwertgefühl</span>, mehr <span class="hl">Lebensfreude</span>,<br>
  mehr <span class="hl">Spaß und Erfolg</span> mit Ihrer Arbeit?</p>

  <div class="abs rule" style="left:73px; top:366px; width:458px;"></div>

  <svg class="abs section-icon" style="left:58px; top:397px;" viewBox="0 0 44 44" aria-hidden="true">
    <circle cx="22" cy="22" r="22" fill="var(--accent)"/>
    <circle cx="22" cy="17" r="6.5" fill="#fff"/>
    <path d="M10 33 C10 26 15 24 22 24 C29 24 34 26 34 33 Z" fill="#fff"/>
  </svg>
  <h2 class="abs section-head" style="left:127px; top:405px;">Zu meiner Person</h2>

  <p class="abs person">Ich bin <strong>Klaus Dieter Wabe</strong>, Transaktionsanalytiker,<br>
  psychotherapeutischer Heilpraktiker und begeis-<br>
  terter Anwender der Leibzentrierten Umdeutungs-<br>
  Methode LUM®.</p>

  <div class="abs rule" style="left:77px; top:608px; width:458px;"></div>

  <div class="abs photo" role="img" aria-label="Foto: Mann mit ausgebreiteten Armen vor Wolkenhimmel und Berglandschaft"></div>

  <p class="abs promise">Gerne helfe ich Ihnen dabei, <strong>gestärkt</strong> aus einer<br>
  Krise hervorzugehen und wieder <strong>mehr Spaß am<br>
  Leben</strong> zu haben. <strong>Gemeinsam</strong> erarbeiten wir<br>
  passende Lösungen für Ihre Probleme, Sie ler-<br>
  nen, Ihre Handlungsmöglichkeiten zu erweitern<br>
  und <strong>neue Wege</strong> zu gehen.</p>

  <svg class="abs quote-mark" width="36" height="36" viewBox="0 0 36 36" aria-hidden="true">
    <circle cx="18" cy="18" r="18" fill="var(--accent)"/>
    <path d="M13 14 L16 14 L12 22 L9 22 Z M20 14 L23 14 L19 22 L16 22 Z" fill="#fff"/>
  </svg>
  <blockquote class="abs quote">Bei aller Ernsthaftigkeit und Empathie dürfen<br>
  Leichtigkeit, Zuversicht und Humor in der Bera-<br>
  tung nicht zu kurz kommen.</blockquote>

  <div class="abs rule" style="left:677px; top:173px; width:457px;"></div>

  <h2 class="abs section-head" style="left:656px; top:219px;">In diesen Bereichen kann ich Sie<br>unterstützen</h2>

  <ul class="abs offer">
    <li>Effektive Kurztherapie</li>
    <li>Coaching zu beruflichen Anliegen</li>
    <li>Auftrittscoaching - Mentales Training</li>
    <li>Entlasung in aktuen Krisen</li>
  </ul>

  <div class="abs rule" style="left:669px; top:575px; width:458px;"></div>

  <h2 class="abs section-head" style="left:656px; top:619px;">Angewandte Methoden</h2>

  <h3 class="abs method-title" style="left:656px; top:688px;">Transaktionsanalyse</h3>
  <p class="abs method-text" style="left:656px; top:732px;">Die TA ist eine Theorie der Persönlichkeit, die menschli-<br>
  ches Verhalten verständlich erklärt. Das zentrale Anliegen<br>
  transaktionsanalytischer Beratung ist es, KlientInnen darin<br>
  zu unterstützen, ihre gewohnte Sicht der Wirklichkeit,<br>
  deren Deutung und die damit verbundenen Verhaltens-<br>
  weisen zu erweitern. Hierbei kann jeder Mensch bei ent-<br>
  sprechender Förderung und Unterstützung selbst heraus-<br>
  finden kann, was für ihn/sie richtig ist.</p>

  <h3 class="abs method-title" style="left:656px; top:940px;">LUM®</h3>
  <p class="abs method-text" style="left:656px; top:983px;">Die Leibzentrierte Umdeutungs-Methode wurde zunächst<br>
  als Zusatztechnik entwickelt, mittlerweile hat sie sich<br>
  zu einem eigenständigen Verfahren weiterentwickelt.<br>
  Kurz: LUM® ist ein Verfahren, um aktuell belastende<br>
  Gefühle (wie Angst oder Stress) zu behandeln und damit<br>
  zusammenhängende Überzeugungen zu verändern. Sie ist<br>
  zudem eine hervorragende Selbsthilfetechnik für die<br>
  Klienten.</p>

</main>
</body>
</html>
```